UI/UX Design for AI Photo-to-Video Web Platform (Figma)

I am looking for a modern, high-converting redesign for my Next.js-based web platform. The service allows users to transform old photos into vibrant memories using AI. The design needs to be clean, intuitive, and "mobile-ready" (responsive).
Key Features to Visualize on the Homepage:
Photo Restoration & Colorization: A clear "before/after" visual showing a black-and-white photo turning into a high-quality color photo.
Photo-to-Video Animation: A visual representation of how both B&W and color photos are transformed into dynamic video clips.
Story Creation: A section showing how these photos and videos are combined into a single "Story Video" with background music.
Scope of Work:
Homepage Redesign: A hero section with the core value proposition and a visual walkthrough of the process.
Service/Internal Pages: Redesigning the functional pages where users upload files and manage their projects.
Responsive Design: While the focus is desktop, the layout must be designed with a "Mobile-First" mindset for easy porting to a mobile app later.
Technical Requirements for the Designer:
Tool: Must be designed in Figma.
Structure: Use Figma Auto Layout and Components for all elements (buttons, inputs, cards).
Design System: Provide a clear style guide (Typography, Color Palette, Spacing).
Assets: All icons should be in SVG format.
Style Preference:
Modern, sleek, and trustworthy.
Since the product is about "memories," the vibe should be emotional yet technologically advanced (AI-driven).

```html
<!DOCTYPE html>
<html lang="en">
<head>
<meta charset="utf-8">
<title>hueframe.ai – Images</title>
<link rel="stylesheet" href="https://fonts.googleapis.com/css2?family=Montserrat:wght@400;500;600;700&display=swap">
<style>
:root{
  --navy:#0f1a3b;
  --navy-deep:#0b1430;
  --line:#23315c;
  --violet:#5b3fe6;
  --violet-2:#6a4cf0;
  --violet-soft:#efecfb;
  --ink:#1d1d2b;
  --muted:#55586a;
  --border:#c9cad3;
  --white:#ffffff;
  --green:#1fb35a;
}
*{box-sizing:border-box;margin:0;padding:0}
html,body{width:1200px;height:2405px;overflow:hidden;background:var(--white);font-family:"Montserrat",sans-serif;color:var(--ink)}
.abs{position:absolute}
.page{position:relative;width:1200px;height:2405px}

/* hero */
.hero{left:0;top:0;width:1200px;height:636px;background:radial-gradient(ellipse at 70% 40%,#15224a 0%,var(--navy) 55%,var(--navy-deep) 100%)}
.topbar{left:0;top:0;width:1200px;height:88px;border-bottom:1px solid var(--line)}
.brand{font-size:30px;font-weight:500;color:var(--white);letter-spacing:.3px}
.topbar .brand{left:110px;top:27px}
.user{left:679px;top:34px;font-size:15px;color:#d5d8e6}
.storage{left:816px;top:34px;font-size:15px;color:#d5d8e6}
.storage b{color:var(--white);font-weight:700}
.credits{left:959px;top:27px;width:130px;height:35px;border:1px solid #4a4fcf;border-radius:4px;background:#1a2355;font-size:13px;color:#c7cae0;display:flex;align-items:center;justify-content:space-between;padding:0 12px}
.credits span:last-child{color:var(--white)}
.tag{left:110px;top:146px;width:295px;height:41px;border:1px solid #5a55e0;border-radius:8px;background:#1e2566;color:#d6d6f5;font-size:17px;display:flex;align-items:center;justify-content:center}
.headline{left:110px;top:203px;font-size:45px;line-height:52px;font-weight:700;color:var(--white)}
.lede{left:110px;top:381px;width:470px;font-size:16px;line-height:26px;color:#e4e6f0}
.btn{display:flex;align-items:center;justify-content:center;gap:7px;border-radius:10px;font-size:15px;font-weight:500;color:var(--white)}
.btn-solid{background:var(--violet)}
.btn-ghost{border:1px solid #6b70c9}
.hero .b1{left:110px;top:449px;width:144px;height:40px}
.hero .b2{left:268px;top:449px;width:184px;height:40px}
.hero .b3{left:465px;top:449px;width:111px;height:40px}
.avatars{left:110px;top:527px;display:flex}
.avatars i{width:42px;height:42px;border-radius:50%;border:2px solid var(--white);margin-right:-9px;display:block}
.trust{left:273px;top:528px;font-size:14px;line-height:21px;color:#e4e6f0}
.stars{color:#f5a623;letter-spacing:-1px;font-size:12px;margin-right:4px}
.compare{left:615px;top:172px;width:476px;height:371px;border:3px solid var(--white);border-radius:20px;overflow:hidden;display:flex}
.compare .bw{width:236px;height:100%;background:linear-gradient(160deg,#9a9a9a,#5a5a5a 60%,#3c3c3c)}
.compare .col{flex:1;height:100%;background:linear-gradient(160deg,#d9c9a6,#8a6a44 55%,#2b2f3d)}
.compare .split{width:4px;background:var(--white)}
.handle{left:836px;top:340px;width:36px;height:36px;border-radius:50%;background:var(--white);display:flex;align-items:center;justify-content:center}

/* cards */
.card{border:1px solid var(--border);border-radius:22px;background:var(--white);overflow:hidden}
.card-title{font-size:26px;font-weight:500}
.card-sub{font-size:15px;color:#333}
.upload{left:111px;top:720px;width:978px;height:400px}
.upload .card-title{left:31px;top:27px}
.upload .card-sub{left:31px;top:69px}
.drop{left:31px;top:121px;width:916px;height:246px;border:1.5px dashed #9a9ca8;border-radius:14px;text-align:center}
.drop h3{font-size:20px;font-weight:500;margin-top:58px}
.drop p{font-size:15px;color:#6a6c78;margin-top:14px}
.select{margin:20px auto 0;width:144px;height:40px;border-radius:10px;background:var(--violet);color:var(--white);font-size:15px;display:flex;align-items:center;justify-content:center}

.gallery{left:111px;top:1183px;width:978px;height:845px}
.gallery .card-title{left:31px;top:27px}
.gallery .card-sub{left:31px;top:73px}
.disclaimer{right:34px;top:55px;font-size:15px;color:var(--violet);display:flex;align-items:center;gap:6px}
.divider{left:42px;top:108px;width:895px;height:2px;background:#d8d9e0}
.band{left:0;top:480px;width:978px;height:365px;background:var(--violet-soft)}
.label{font-size:16px;color:#333;display:flex;align-items:center;gap:6px}
.frame{width:206px;height:243px;border:1px solid #9fa1ab;border-radius:4px;background:var(--white);overflow:hidden}
.frame .ph{position:absolute;left:0;top:38px;width:100%;height:165px}
.ph-bw{background:linear-gradient(135deg,#8d8d8d,#3d3d3d 55%,#6a6a6a)}
.ph-col{background:linear-gradient(135deg,#8a8f5a,#2d3446 50%,#a8724e)}
.frame .empty{position:absolute;inset:0;display:flex;align-items:center;justify-content:center;font-size:16px}
.dl{position:absolute;right:13px;bottom:10px;width:21px;height:21px;border-radius:5px;background:var(--violet-2);display:flex;align-items:center;justify-content:center}
.action{width:228px;height:40px;border:1px solid var(--violet);border-radius:10px;color:var(--violet);font-size:15px;display:flex;align-items:center;justify-content:center;background:var(--white)}
.action.primary{background:var(--violet);color:var(--white)}
.gen{font-size:16px;line-height:19px;color:#333}

/* footer */
.footer{left:0;top:2114px;width:1200px;height:291px;background:var(--navy)}
.footer .brand{left:112px;top:54px}
.socials{left:114px;top:99px;display:flex;gap:4px}
.socials i{width:21px;height:21px;border:1.5px solid var(--white);border-radius:3px;display:block}
.fcol{color:var(--white)}
.fcol h4{font-size:19px;font-weight:500;margin-bottom:13px}
.fcol a{display:block;font-size:15px;color:#d8dbe8;text-decoration:none;margin-bottom:8px}
.news{left:787px;top:62px}
.news p{font-size:15px;color:#d8dbe8}
.email{left:788px;top:128px;width:301px;height:40px;border:1px solid #8b90b5;border-radius:8px;color:var(--white);font-size:14px;display:flex;align-items:center;justify-content:space-between;padding:0 10px}
.frule{left:0;top:224px;width:1200px;height:1px;background:var(--line)}
.copy{left:0;top:244px;width:1200px;text-align:center;font-size:13px;color:#d8dbe8}
</style>
</head>
<body>
<div class="page">

<section class="hero abs">
  <header class="topbar abs">
    <div class="brand abs">hueframe.ai</div>
    <div class="user abs">Mira Tann</div>
    <div class="storage abs"><b>114 MB</b>/1.0 GB</div>
    <div class="credits abs"><span>Credits</span><span>4,740</span></div>
  </header>
  <div class="tag abs">AI Photo-to-Video Platform</div>
  <h1 class="headline abs">Bring Your<br>Old Memories<br>Back to Life</h1>
  <p class="lede abs">Restore, colorize, and animate your photos into stunning cinematic videos using AI.</p>
  <div class="btn btn-solid b1 abs">
    <svg width="11" height="14" viewBox="0 0 11 14"><path d="M1 0h6l4 4v10H1z" fill="#fff"/><circle cx="5.5" cy="8" r="2" fill="#5b3fe6"/></svg>Images</div>
  <div class="btn btn-ghost b2 abs">
    <svg width="11" height="14" viewBox="0 0 11 14"><path d="M0 0h7l4 4v10H0z" fill="#fff"/><path d="M4 6l3 2-3 2z" fill="#0f1a3b"/></svg>Video animations</div>
  <div class="btn btn-ghost b3 abs">
    <svg width="15" height="13" viewBox="0 0 15 13"><rect x="1" y="1" width="13" height="11" rx="1.5" fill="none" stroke="#fff" stroke-width="1.6"/><path d="M4 1v11M11 1v11M1 6.5h13" stroke="#fff" stroke-width="1.4"/></svg>Studio</div>
  <div class="avatars abs">
    <i role="img" aria-label="User portrait" style="background:#c89a7a"></i>
    <i role="img" aria-label="User portrait" style="background:#a57b60"></i>
    <i role="img" aria-label="User portrait" style="background:#d79a5a"></i>
    <i role="img" aria-label="User portrait" style="background:#7d8a8c"></i>
  </div>
  <div class="trust abs">Trusted by 100,000+ users<br><span class="stars">★★★★★</span>4.9/5 from 2,300+ reviews</div>
  <div class="compare abs">
    <div class="bw" role="img" aria-label="Black and white photo of a young man and a girl standing together"></div>
    <div class="split"></div>
    <div class="col" role="img" aria-label="The same photo restored and colorized"></div>
  </div>
  <div class="handle abs"><svg width="20" height="14" viewBox="0 0 20 14"><path d="M7 1L2 7l5 6M13 1l5 6-5 6" fill="none" stroke="#1d1d2b" stroke-width="2"/></svg></div>
</section>

<section class="card upload abs">
  <h2 class="card-title abs">Upload Images</h2>
  <p class="card-sub abs">Upload photos to generate vintage and real color versions</p>
  <div class="drop abs">
    <h3>Drag and drop images here</h3>
    <p>Maximum 20 images 100MB total JPG, PNG, GIF, TIFF up to 10MB each</p>
    <div class="select">Select files</div>
  </div>
</section>

<section class="card gallery abs">
  <div class="band abs"></div>
  <h2 class="card-title abs">Images</h2>
  <p class="card-sub abs">Each row shows Original, Vintage Color, and Real Color.</p>
  <div class="disclaimer abs"><svg width="15" height="15" viewBox="0 0 15 15"><circle cx="7.5" cy="7.5" r="7.5" fill="#5b3fe6"/><path d="M7.5 6.5v4.5" stroke="#fff" stroke-width="1.6"/><circle cx="7.5" cy="4.2" r="1" fill="#fff"/></svg>AI Disclaimer</div>
  <div class="divider abs"></div>

  <div class="label abs" style="left:27px;top:153px">Original ID: OLOGYDYS</div>
  <div class="label abs" style="left:257px;top:153px">Vintage</div>
  <div class="label abs" style="left:486px;top:153px">Real</div>
  <div class="frame abs" style="left:28px;top:188px">
    <div class="ph ph-bw" role="img" aria-label="Black and white family photo"></div>
    <div class="dl"><svg width="11" height="11" viewBox="0 0 11 11"><circle cx="5.5" cy="5.5" r="4.8" fill="none" stroke="#fff" stroke-width="1.2"/><path d="M5.5 2.8v5M3.5 6l2 2 2-2" fill="none" stroke="#fff" stroke-width="1.2"/></svg></div>
  </div>
  <div class="frame abs" style="left:258px;top:188px"><div class="empty">Not generated</div></div>
  <div class="frame abs" style="left:487px;top:188px"><div class="empty">Not generated</div></div>
  <div class="action abs" style="left:716px;top:285px">Rotate</div>
  <div class="action abs" style="left:716px;top:338px">Delete</div>
  <div class="action primary abs" style="left:716px;top:391px">Generata (20)</div>

  <div class="label abs" style="left:27px;top:521px">Original ID: OLOGYDYS</div>
  <div class="label abs" style="left:257px;top:521px">Vintage <svg width="16" height="16" viewBox="0 0 16 16"><circle cx="8" cy="8" r="8" fill="#1fb35a"/><path d="M4.5 8.2l2.3 2.3 4.5-4.6" fill="none" stroke="#fff" stroke-width="1.8"/></svg></div>
  <div class="label abs" style="left:486px;top:521px">Real <svg width="16" height="16" viewBox="0 0 16 16"><circle cx="8" cy="8" r="8" fill="#1fb35a"/><path d="M4.5 8.2l2.3 2.3 4.5-4.6" fill="none" stroke="#fff" stroke-width="1.8"/></svg></div>
  <div class="frame abs" style="left:28px;top:556px">
    <div class="ph ph-bw" role="img" aria-label="Black and white family photo"></div>
    <div class="dl"><svg width="11" height="11" viewBox="0 0 11 11"><circle cx="5.5" cy="5.5" r="4.8" fill="none" stroke="#fff" stroke-width="1.2"/><path d="M5.5 2.8v5M3.5 6l2 2 2-2" fill="none" stroke="#fff" stroke-width="1.2"/></svg></div>
  </div>
  <div class="frame abs" style="left:257px;top:556px">
    <div class="ph ph-col" style="top:30px;height:173px" role="img" aria-label="Family photo in vintage color"></div>
    <div class="dl"><svg width="11" height="11" viewBox="0 0 11 11"><circle cx="5.5" cy="5.5" r="4.8" fill="none" stroke="#fff" stroke-width="1.2"/><path d="M5.5 2.8v5M3.5 6l2 2 2-2" fill="none" stroke="#fff" stroke-width="1.2"/></svg></div>
  </div>
  <div class="frame abs" style="left:486px;top:556px">
    <div class="ph ph-col" style="top:30px;height:173px" role="img" aria-label="Family photo in real color"></div>
    <div class="dl"><svg width="11" height="11" viewBox="0 0 11 11"><circle cx="5.5" cy="5.5" r="4.8" fill="none" stroke="#fff" stroke-width="1.2"/><path d="M5.5 2.8v5M3.5 6l2 2 2-2" fill="none" stroke="#fff" stroke-width="1.2"/></svg></div>
  </div>
  <div class="gen abs" style="left:715px;top:704px">Generation time:<br>3m 2s</div>
  <div class="action abs" style="left:716px;top:759px">Delete</div>
</section>

<footer class="footer abs">
  <div class="brand abs">hueframe.ai</div>
  <div class="socials abs"><i></i><i></i><i></i><i></i></div>
  <div class="fcol abs" style="left:319px;top:58px"><h4>Product</h4><a>Features</a><a>How it works</a><a>Pricing</a><a>API</a></div>
  <div class="fcol abs" style="left:470px;top:58px"><h4>Company</h4><a>About us</a><a>Biog</a><a>Careers</a><a>Contact us</a></div>
  <div class="fcol abs" style="left:623px;top:58px"><h4>Support</h4><a>Help Center</a><a>Tutorials</a><a>Community</a><a>Privacy Policy</a></div>
  <div class="fcol news abs"><h4>Subscribe To Our&nbsp; Newsletter</h4><p>Get tips, updates &amp; special offers.</p></div>
  <div class="email abs"><span>Enter your email</span><svg width="8" height="10" viewBox="0 0 8 10"><path d="M1 0l6 5-6 5z" fill="#fff"/></svg></div>
  <div class="frule abs"></div>
  <div class="copy abs">Copyright © 2026 hueframe.ai. All rights reserved.</div>
</footer>

</div>
</body>
</html>
```